Modern Yoga Studio Timetable and Flyer Design

We have a comprehensive class timetable and we are wanting to a clean modern look for our Spring timetable.

We require a double sided flyer with our class timetable included.
We would prefer an A5 size (postcard) or DL (1/3 A4).

We would like the final flyer to have.
Side A : Yoga image, logo

Fennel Stretch Hall
address: 4/71 Wexcombe Lane, Pelharton
website: fennelstretch.com.au
mobile: 0471 296 814

Side B: Clear easy to read timetable with a break down of class types and website.

We would also like to have a copy of the timetable itself as a separate jpg or pdf for use on our website to download.

Thank you.
Yours kindly,
Nell

I have attached a sample of another timetable of which I like the look and feel of, however this is just a guide. I've also attached our 'new' schedule in WORD plus uploaded our last design of the front.
Updates

Target Market(s)

Women aged 30-45

Industry/Entity Type

Health And Wellness

Font styles to use
Other font styles liked:
• Brandon Grotesque, Jenna Sue

Colors
6c459b
33a6d7
ffffff

Requirements
Must have
• A definitive colour to decipher between different class types on our timetable. Where each colour represents a different class type. Colours and layouts similar to our website design, see www.fennelstretch.com.au
Nice to have
• I've included a design of another studio whose timetable design I like. One of our own yoga images instead of a stock image.
Should not have
• No dark gridlines between the cells/boxes in the timetables. Please don't use stock yoga images.

```html
<!DOCTYPE html>
<html lang="en">
<head>
<meta charset="utf-8">
<title>Fennel Stretch Spring Timetable</title>
<link href="https://fonts.googleapis.com/css2?family=Source+Sans+3:wght@400;600;700&display=swap" rel="stylesheet">
<style>
:root{
  --purple:#6c459b;
  --blue:#33a6d7;
  --blue-light:#8fcfec;
  --purple-light:#a68bc6;
  --white:#ffffff;
  --wall-top:#cdbfd3;
  --wall-mid:#c4b3c2;
  --floor:#9c7a66;
}
*{margin:0;padding:0;box-sizing:border-box}
html,body{width:1200px;height:835px;overflow:hidden;background:var(--white)}
.timetable{
  position:relative;width:1200px;height:835px;overflow:hidden;
  font-family:"Source Sans 3","Myriad Pro",Arial,sans-serif;
}
.studio-photo{
  position:absolute;inset:0;
  background:
    radial-gradient(ellipse 330px 260px at 560px 360px,rgba(120,70,150,.35),transparent 70%),
    radial-gradient(ellipse 260px 300px at 760px 330px,rgba(190,110,80,.30),transparent 70%),
    linear-gradient(180deg,var(--wall-top) 0%,var(--wall-mid) 66%,#a98e7c 74%,var(--floor) 100%);
}
.veil{
  position:absolute;left:22px;top:0;width:1152px;height:812px;
  background:rgba(255,255,255,.55);
}
.title{
  position:absolute;left:0;right:0;top:14px;text-align:center;
  color:var(--purple);font-weight:700;font-size:25px;letter-spacing:.3px;
}
.day{
  position:absolute;top:74px;width:90px;margin-left:-45px;text-align:center;
  color:var(--purple);font-weight:700;font-size:20px;
}
.time{
  position:absolute;left:78px;width:110px;margin-top:-12px;
  color:var(--blue);font-weight:700;font-size:19px;
}
.class{
  position:absolute;display:flex;align-items:center;justify-content:center;
  text-align:center;color:var(--white);font-weight:400;font-size:17px;
  line-height:1.15;text-transform:uppercase;
}
.class.purple{background:var(--purple)}
.class.blue{background:var(--blue)}
.class.kids{background:var(--blue-light)}
.class.teens{background:var(--purple-light)}
.class.circle{width:86px;height:86px;border-radius:50%}
.class.pill{border-radius:24px}
.class.slant{clip-path:polygon(6% 0,100% 0,94% 100%,0 100%)}
.studio-details{
  position:absolute;left:40px;top:770px;color:var(--purple);
}
.studio-name{font-weight:700;font-size:19px;line-height:1.1}
.studio-contact{font-weight:600;font-size:14px;color:var(--purple)}
.legend{
  position:absolute;left:470px;top:776px;display:flex;gap:18px;
  list-style:none;color:var(--purple);font-weight:600;font-size:14px;
}
.legend li{display:flex;align-items:center;gap:6px}
.swatch{width:14px;height:14px;display:inline-block}
.note{
  position:absolute;right:48px;top:772px;color:var(--purple);
  font-weight:700;font-size:19px;
}
</style>
</head>
<body>
<main class="timetable">
  <div class="studio-photo" role="img" aria-label="Studio photo of a woman in downward-facing dog on a woven mat"></div>
  <div class="veil"></div>

  <h1 class="title">FENNEL STRETCH SPRING TIMETABLE</h1>

  <div class="day" style="left:243px">MON</div>
  <div class="day" style="left:372px">TUE</div>
  <div class="day" style="left:498px">WED</div>
  <div class="day" style="left:627px">THU</div>
  <div class="day" style="left:753px">FRI</div>
  <div class="day" style="left:883px">SAT</div>
  <div class="day" style="left:1013px">SUN</div>

  <div class="time" style="top:132px">0545AM</div>
  <div class="time" style="top:184px">0900AM</div>
  <div class="time" style="top:230px">0915AM</div>
  <div class="time" style="top:281px">0930AM</div>
  <div class="time" style="top:329px">1030AM</div>
  <div class="time" style="top:380px">1100AM</div>
  <div class="time" style="top:426px">1215AM</div>
  <div class="time" style="top:476px">0400PM</div>
  <div class="time" style="top:522px">0445PM</div>
  <div class="time" style="top:568px">0500PM</div>
  <div class="time" style="top:618px">0600PM</div>
  <div class="time" style="top:669px">0615PM</div>
  <div class="time" style="top:718px">0730PM</div>

  <div class="class blue slant" style="left:306px;top:112px;width:138px;height:41px">RISE + SHINE*</div>
  <div class="class blue slant" style="left:567px;top:112px;width:135px;height:41px">RISE + SHINE*</div>

  <div class="class purple circle" style="left:326px;top:187px">VINYASA<br>FLOW</div>
  <div class="class blue circle" style="left:196px;top:236px">SLOW<br>FLOW</div>
  <div class="class purple circle" style="left:589px;top:236px">VINYASA<br>FLOW</div>
  <div class="class purple circle" style="left:840px;top:136px">VINYASA<br>FLOW</div>
  <div class="class blue pill" style="left:948px;top:204px;width:131px;height:47px">YIN</div>

  <div class="class purple" style="left:822px;top:300px;width:129px;height:46px">PREGNANCY*</div>
  <div class="class blue" style="left:305px;top:350px;width:134px;height:46px">MUM + BABY*</div>
  <div class="class blue" style="left:563px;top:350px;width:126px;height:46px">MUM + BABY*</div>
  <div class="class purple" style="left:563px;top:401px;width:126px;height:44px">PREGNANCY</div>

  <div class="class purple circle" style="left:840px;top:433px">VINYASA<br>FLOW</div>
  <div class="class kids" style="left:437px;top:448px;width:115px;height:44px">KIDS 8-12*</div>
  <div class="class kids" style="left:563px;top:448px;width:126px;height:44px">KIDS 5-7*</div>
  <div class="class teens" style="left:437px;top:498px;width:115px;height:45px">TEENS<br>12-16*</div>
  <div class="class teens" style="left:563px;top:546px;width:126px;height:43px">TEENS<br>12-16*</div>

  <div class="class purple" style="left:180px;top:594px;width:128px;height:44px">PREGNANCY*</div>
  <div class="class purple circle" style="left:326px;top:571px">VINYASA<br>FLOW</div>
  <div class="class blue circle" style="left:455px;top:571px">SLOW<br>FLOW</div>
  <div class="class blue pill" style="left:691px;top:592px;width:131px;height:46px">FLOW +<br>RESTORE</div>
  <div class="class purple" style="left:563px;top:638px;width:126px;height:45px">PREGNANCY*</div>

  <div class="class purple circle" style="left:204px;top:675px">VINYASA<br>FLOW</div>
  <div class="class purple" style="left:305px;top:689px;width:134px;height:45px">PREGNANCY*</div>
  <div class="class blue pill" style="left:437px;top:689px;width:125px;height:45px">YIN +<br>RESTORE</div>
  <div class="class blue pill" style="left:563px;top:689px;width:126px;height:45px">WOMEN'S<br>WELLNESS*</div>

  <div class="studio-details">
    <p class="studio-name">Fennel Stretch Hall</p>
    <p class="studio-contact">4/71 Wexcombe Lane, Pelharton · 0471 296 814 · fennelstretch.com.au</p>
  </div>

  <ul class="legend">
    <li><span class="swatch" style="background:var(--purple)"></span>Vinyasa + Pregnancy</li>
    <li><span class="swatch" style="background:var(--blue)"></span>Gentle + Restore</li>
    <li><span class="swatch" style="background:var(--blue-light)"></span>Kids</li>
    <li><span class="swatch" style="background:var(--purple-light)"></span>Teens</li>
  </ul>

  <p class="note">* bookings essential</p>
</main>
</body>
</html>
```